Firma Rusow Innenausbau
Zielgruppe
Wir bieten unserem Kunden den gesamten Innenausbau an. Böden, Wände, Decken, Trockenbau Türen, Speziell auch Spanndecken siehe auch www.rusow-Innenausbau.de
Zielgruppe sind Privatleute sowie Bauunternehmer und Bauträger.
Aufgabenstellung
Die Visitenkarten sollen unseren modernen Stil wie auf der HP sowie auf unseren Autos haben.

```html
<!DOCTYPE html>
<html lang="de">
<head>
<meta charset="utf-8">
<title>Rusow Innenausbau – Visitenkarten</title>
<link href="https://fonts.googleapis.com/css2?family=Open+Sans:wght@400;600;700&family=Kalam:wght@400;700&display=swap" rel="stylesheet">
<style>
  :root {
    --bg: #d9d6cc;
    --card-dark: #050505;
    --card-light: #ffffff;
    --orange: #e8630f;
    --brown: #6b2c0c;
    --text-light: #f4f4f4;
  }
  * { margin: 0; padding: 0; box-sizing: border-box; }
  html, body { width: 1200px; height: 900px; overflow: hidden; }
  body { background: var(--bg); font-family: "Open Sans", Arial, sans-serif; position: relative; }

  .card {
    position: absolute; width: 640px; height: 414px; overflow: hidden;
    background: var(--card-dark); box-shadow: 0 6px 18px rgba(0,0,0,.25);
  }
  .card--services { left: 80px; top: 30px; }
  .card--contact { left: 480px; top: 456px; }

  /* brand wordmark */
  .brand { position: absolute; display: flex; align-items: center; gap: 14px; }
  .brand__square { width: 24px; height: 24px; background: var(--orange); flex: none; }
  .brand__name { font-weight: 600; font-size: 30px; line-height: 1.15; }
  .card--services .brand { left: 40px; top: 140px; max-width: 280px; }
  .card--services .brand__name { color: var(--text-light); }
  .card--contact .brand { left: 360px; top: 130px; }
  .card--contact .brand__name { color: var(--brown); font-size: 26px; }

  .slogan { position: absolute; font-family: "Kalam", cursive; font-size: 24px; }
  .card--services .slogan { left: 40px; bottom: 40px; color: var(--orange); }
  .card--contact .slogan { right: 40px; top: 220px; color: var(--brown); text-align: right; line-height: 1.3; }

  /* services */
  .services { position: absolute; left: 350px; top: 34px; width: 270px; }
  .services__title { color: var(--orange); font-size: 21px; font-weight: 400; margin-bottom: 2px; }
  .services__list { list-style: none; margin-bottom: 18px; }
  .services__list li { color: var(--text-light); font-size: 14px; line-height: 1.45; padding-left: 20px; position: relative; }
  .services__list li::before { content: "★"; color: var(--orange); position: absolute; left: 0; font-size: 12px; top: 1px; }

  /* contact */
  .contact-shape { position: absolute; inset: 0; }
  .contact { position: absolute; left: 40px; top: 110px; color: var(--text-light); }
  .contact__name { color: var(--orange); font-size: 26px; font-weight: 700; }
  .contact__role { font-size: 16px; margin-bottom: 26px; }
  .contact__address { font-size: 16px; line-height: 1.4; font-style: normal; margin-bottom: 14px; }
  .contact__list { list-style: none; }
  .contact__list li { display: flex; align-items: center; gap: 12px; font-size: 16px; line-height: 1.55; }
  .contact__icon { width: 16px; height: 16px; flex: none; fill: var(--orange); }
</style>
</head>
<body>

<section class="card card--services">
  <div class="brand">
    <span class="brand__square"></span>
    <span class="brand__name">Rusow<br>Innenausbau</span>
  </div>
  <p class="slogan">Wir modernisieren Ihr Zuhause!</p>

  <div class="services">
    <h2 class="services__title">Trockenbau</h2>
    <ul class="services__list">
      <li>Trennwände</li>
      <li>abgehängte Decken</li>
      <li>Brandschutz</li>
      <li>Türen Bauelemente</li>
      <li>Mineralfaserdecken</li>
    </ul>
    <h2 class="services__title">Spanndecken</h2>
    <ul class="services__list">
      <li>10 Jahre Herstellergarantie</li>
      <li>Einbau an nur einem Tag</li>
      <li>Pflegeleichtes Material</li>
      <li>Badezimmer geeignet</li>
      <li>Decke muss nie mehr<br>gestrichen werden</li>
    </ul>
  </div>
</section>

<section class="card card--contact">
  <svg class="contact-shape" viewBox="0 0 640 414" aria-hidden="true">
    <path d="M292 236 C350 340 450 392 560 414 H500 C410 390 335 330 292 236 Z" fill="var(--orange)"/>
    <path d="M250 0 H640 V414 H570 C400 385 262 230 250 0 Z" fill="var(--card-light)"/>
  </svg>

  <div class="brand">
    <span class="brand__square"></span>
    <span class="brand__name">Rusow<br>Innenausbau</span>
  </div>
  <p class="slogan">Kreativ individuell<br>&amp; effizient!</p>

  <div class="contact">
    <h1 class="contact__name">Jonas Rusow</h1>
    <p class="contact__role">Geschäftsführer</p>
    <address class="contact__address">Lindenallee 12<br>41800 Birkenfeld</address>
    <ul class="contact__list">
      <li><svg class="contact__icon" viewBox="0 0 16 16"><path d="M3 1l3 3-2 2c1 2 3 4 5 5l2-2 3 3-2 3C7 15 1 9 1 3z"/></svg>0 21 00 / 45 61 230</li>
      <li><svg class="contact__icon" viewBox="0 0 16 16"><path d="M4 1h8v14H4z M5.5 3v8h5V3z" fill-rule="evenodd"/></svg>0151 / 98 76 54 32</li>
      <li><svg class="contact__icon" viewBox="0 0 16 16"><path d="M1 3h14v10H1z M2 4l6 5 6-5" stroke="var(--card-dark)" stroke-width="1"/></svg>info@rusow-bau.de</li>
      <li><svg class="contact__icon" viewBox="0 0 16 16"><circle cx="8" cy="8" r="7"/><path d="M1 8h14M8 1c-3 4-3 10 0 14M8 1c3 4 3 10 0 14" stroke="var(--card-dark)" fill="none" stroke-width="1"/></svg>www.rusow-innenausbau.de</li>
    </ul>
  </div>
</section>

</body>
</html>
```